Design for a very long wall that will be wall printed. The name of the facility is "Bright Gallery"

The space I am working on has a 30' x 8' wall. It is a wall that is located in a under construction Design Showroom where contractors of all trades can have an office and put out their banners and different items for customers to come and see. so there could be roofers, construction, cabinet installers and designers, gutters and other trades can rent an office in the space and bring their customers and sit down and talk about what they need. I want the design for the wall to have a bold punch and it will be printed on the wall with a high definition wall printer. The walls are arctic white right now and I can send the color codes for the color the wall is currently. The wall printer has the capability to do white as well. I am including some pics of the space and an example wall print.

Target Market(s)

Contractors and Customers of Contractors

Industry/Entity Type

all trades. Photos are to demonstrate the capabilities of the printer that will be used

Requirements
Must have
• Perhaps have a person or persons int he design, a human element and perhaps some abstract elements as well
Nice to have
• Perhaps some architecture or perhaps an interior cabinet or fixtures. Glass doors and or walls. Perhaps incorporate the name "Bright Gallery"

```html
<!DOCTYPE html>
<html lang="en">
<head>
<meta charset="utf-8">
<title>Bright Gallery – Wall Print</title>
<link rel="stylesheet" href="https://fonts.googleapis.com/css2?family=Russo+One&display=swap">
<style>
  :root {
    --paper: #ffffff;
    --brand-blue: #3a68ac;
    --accent-orange: #f4a583;
    --panel-grey: #eef1f4;
    --blueprint-faint: #f7f5f5;
    --art-deep: #4f77b3;
    --art-mid: #9db6d8;
    --art-light: #e6edf6;
  }
  * { margin: 0; padding: 0; box-sizing: border-box; }
  html, body {
    width: 1200px; height: 363px; overflow: hidden; background: var(--paper);
  }
  .wall-print {
    position: relative; width: 1200px; height: 363px; overflow: hidden;
    background: linear-gradient(90deg, var(--paper) 0%, var(--blueprint-faint) 40%, var(--paper) 66%);
  }
  .art-worker {
    position: absolute; left: 30px; top: 12px; width: 266px; height: 332px;
    background:
      linear-gradient(180deg, rgba(255,255,255,0.55) 0%, rgba(255,255,255,0) 35%),
      linear-gradient(160deg, var(--art-light) 0%, var(--art-mid) 45%, var(--art-deep) 100%);
  }
  .city-panel {
    position: absolute; left: 800px; top: 0; width: 400px; height: 363px;
    background: linear-gradient(90deg, var(--panel-grey) 0%, #f5f7f9 100%);
  }
  .art-city {
    position: absolute; left: 40px; top: 12px; width: 348px; height: 332px;
    background:
      linear-gradient(180deg, rgba(255,255,255,0.6) 0%, rgba(255,255,255,0) 40%),
      linear-gradient(200deg, var(--art-light) 0%, var(--art-mid) 50%, var(--art-deep) 100%);
  }
  .accent-lines { position: absolute; inset: 0; width: 1200px; height: 363px; }
  .accent-lines line { stroke: var(--accent-orange); stroke-width: 2.4; }
  .facility-name {
    position: absolute; left: 0; top: 0; width: 1174px; height: 363px;
    text-align: center; z-index: 2;
    font-family: "Russo One", sans-serif; font-weight: 400;
    text-transform: uppercase; line-height: 1; letter-spacing: 0;
  }
  .facility-name__line {
    position: absolute; left: 0; display: block; width: 100%;
    transform: skewX(-14deg);
    color: var(--brand-blue); font-size: 108px;
  }
  .facility-name__line::before {
    content: attr(data-text); position: absolute; left: 6px; top: -6px; width: 100%;
    color: transparent; -webkit-text-stroke: 1px var(--brand-blue); z-index: -1;
  }
  .facility-name__line--top { top: 76px; }
  .facility-name__line--bottom { top: 170px; }
</style>
</head>
<body>
  <main class="wall-print">
    <div class="art-worker" role="img" aria-label="Watercolour illustration of a construction worker in a hard hat beside scaffolding sketches"></div>
    <div class="city-panel">
      <div class="art-city" role="img" aria-label="Blueprint-style illustration of futuristic skyscrapers on a curved architectural plan"></div>
    </div>

    <svg class="accent-lines" viewBox="0 0 1200 363" aria-hidden="true">
      <line x1="616" y1="46" x2="857" y2="46"/>
      <line x1="597" y1="53" x2="773" y2="53"/>
      <line x1="567" y1="60" x2="808" y2="60"/>
      <line x1="608" y1="68" x2="847" y2="68"/>
      <line x1="328" y1="294" x2="568" y2="294"/>
      <line x1="377" y1="308" x2="618" y2="308"/>
      <line x1="338" y1="316" x2="578" y2="316"/>
    </svg>

    <h1 class="facility-name">
      <span class="facility-name__line facility-name__line--top" data-text="Bright">Bright</span>
      <span class="facility-name__line facility-name__line--bottom" data-text="Gallery">Gallery</span>
    </h1>
  </main>
</body>
</html>
```